Business Card / Flyer Design Project

Prevent Accidents in your HomeSafety grab barsChild safety and child proofingEarthquake proofingOur company provide a service to help prevent home accidents of all types, from bathroom slip and fall accidents to baby proofing and earthquake safety. Maybe a 4x6 flyer type would be the best for handouts? Maybe a graphic of some kind? Company name, Dwelling Guard Crew. Contractors license # 731562

Contact Information for Business Card

Thad Friday818-419-4212

```html
<!DOCTYPE html>
<html lang="en">
<head>
<meta charset="utf-8">
<title>Dwelling Guard Crew — Card</title>
<link href="https://fonts.googleapis.com/css2?family=Questrial&display=swap" rel="stylesheet">
<style>
  :root {
    --panel: #535553;
    --panel-text: #ffffff;
    --ink: #4a4a4c;
    --bg: #ffffff;
  }
  html, body {
    margin: 0;
    padding: 0;
    overflow: hidden;
    background: var(--bg);
  }
  .canvas {
    position: relative;
    width: 1200px;
    height: 1000px;
    overflow: hidden;
    background: var(--bg);
    font-family: "Questrial", sans-serif;
    font-variant: small-caps;
    letter-spacing: 0.04em;
  }
  .panel {
    position: absolute;
    width: 252px;
    height: 252px;
    background: var(--panel);
    color: var(--panel-text);
  }
  .panel--front { left: 366px; top: 170px; }
  .panel--back { left: 365px; top: 614px; }

  .brand {
    position: absolute;
    left: 10px;
    right: 10px;
    top: 112px;
    font-size: 20px;
    letter-spacing: 0.02em;
    text-align: center;
    white-space: nowrap;
    padding-bottom: 5px;
    border-bottom: 3px solid var(--panel-text);
  }
  .tagline {
    position: absolute;
    left: 30px;
    right: 8px;
    top: 112px;
    font-size: 18px;
    line-height: 18px;
    letter-spacing: 0.03em;
    white-space: nowrap;
  }
  .contact {
    position: absolute;
    left: 675px;
    top: 283px;
    color: var(--ink);
    font-size: 18px;
    line-height: 24px;
  }
  .contact__phone { font-variant: normal; font-size: 17px; letter-spacing: 0.1em; }
  .services {
    position: absolute;
    left: 647px;
    top: 680px;
    margin: 0;
    padding: 0;
    list-style: none;
    color: var(--ink);
    font-size: 18px;
    line-height: 19px;
    letter-spacing: 0.03em;
    white-space: nowrap;
  }
  .services li { margin-bottom: 7px; }
</style>
</head>
<body>
<div class="canvas">
  <section class="panel panel--front">
    <div class="brand">Dwelling Guard Crew</div>
  </section>
  <div class="contact">
    <div class="contact__name">Orin Calloway</div>
    <div class="contact__phone">555-302-7186</div>
  </div>

  <section class="panel panel--back">
    <div class="tagline">We help prevent home<br>accidents of all types</div>
  </section>
  <ul class="services">
    <li>Bathroom slip and<br>fall accidance</li>
    <li>Safety grab bars</li>
    <li>Child safety<br>and child proofing</li>
    <li>Earthquake proofing</li>
  </ul>
</div>
</body>
</html>
```